Business Card Design for ClearPathVitality

We need the new logo on a business card for 3 employees:
Nora Kettering, PhD, Advanced Instructor and Practitioner of SomaLink Integral Medicine (email: nora@clearpathvitality.com)
Ray Holm, Business Manager (email: ray@clearpathvitality.com)
Bea Marlowe, Administrative Assistant (email: bea@helixsense.com)

Target Market(s)

healthcare professionals

Industry/Entity Type

Alternative Medicine

Contact Information for Business Card

Names, titles, emails (names, titles, emails are in project description), phone, address, website, with logo and tagline. See below for address, phone, website: 418 Alder Ln, Bldg 12, Ste 305
Santa Cruz, CA 95060
831-555-2746
www.clearpathvitality.com
Tagline: Roots of Balance, Light of Renewal

Font styles to use
Other font styles liked:
• Gabriela

Colors
00a990
86cfc6
6b449b
b7a5cd
85abd2
abd036

Requirements
Must have
• Colors and style that match the logo design - shades such as blue, green, purple
• Compatible or same font as in the logo
Nice to have
• Nice if it goes with the theme of Nora's last business card - uploaded below
Should not have
• colors or style in conflict with the logo

```html
<!DOCTYPE html>
<html lang="en">
<head>
<meta charset="utf-8">
<title>ClearPathVitality Business Cards</title>
<link href="https://fonts.googleapis.com/css2?family=Roboto:wght@400;500;700&display=swap" rel="stylesheet">
<style>
  :root {
    --stage: #2b2b2b;
    --card: #ffffff;
    --ink: #1a1a1a;
    --muted: #555555;
    --navy: #23408e;
    --green: #4cb848;
    --purple: #3d2a7a;
    --teal: #00a990;
  }
  html, body {
    margin: 0;
    width: 1200px;
    height: 900px;
    overflow: hidden;
    background: var(--stage);
    font-family: "Roboto", Arial, sans-serif;
  }
  .stage {
    position: relative;
    width: 1200px;
    height: 900px;
  }
  .card {
    position: absolute;
    left: 280px;
    width: 640px;
    height: 366px;
    background: var(--card);
    border-radius: 16px;
    box-shadow: 0 10px 28px rgba(0,0,0,0.55);
    overflow: hidden;
  }
  .card--front { top: 60px; }
  .card--back { top: 474px; }

  .brand {
    display: flex;
    align-items: center;
    gap: 18px;
  }
  .brand__mark {
    border-radius: 50%;
    background: linear-gradient(135deg, var(--purple), var(--teal) 60%, var(--green));
    flex: none;
  }
  .brand__name {
    font-weight: 500;
    color: var(--purple);
    letter-spacing: 0.5px;
  }

  .card--front .brand {
    position: absolute;
    left: 0; right: 0;
    top: 118px;
    justify-content: center;
  }
  .card--front .brand__mark { width: 104px; height: 104px; }
  .card--front .brand__name { font-size: 40px; }
  .front__tagline {
    position: absolute;
    left: 0; right: 0;
    top: 238px;
    text-align: center;
    font-size: 15px;
    letter-spacing: 2px;
    color: var(--muted);
  }
  .front__web {
    position: absolute;
    left: 0; right: 0;
    bottom: 40px;
    text-align: center;
    font-size: 15px;
    color: var(--ink);
  }

  .card--back .brand {
    position: absolute;
    left: 46px;
    top: 40px;
    gap: 14px;
  }
  .card--back .brand__mark { width: 78px; height: 78px; }
  .card--back .brand__name { font-size: 30px; }

  .person {
    position: absolute;
    left: 60px;
    top: 166px;
  }
  .person__name {
    font-size: 22px;
    font-weight: 700;
    letter-spacing: 0.3px;
  }
  .person__first { color: var(--navy); }
  .person__last { color: var(--green); }
  .person__title {
    font-size: 12px;
    font-weight: 500;
    color: var(--ink);
    margin-top: 2px;
  }
  .divider {
    position: absolute;
    left: 56px;
    right: 46px;
    top: 222px;
    height: 3px;
    background: var(--navy);
  }
  .contacts {
    position: absolute;
    left: 60px;
    top: 240px;
    margin: 0;
    padding: 0;
    list-style: none;
  }
  .contacts li {
    display: flex;
    align-items: center;
    gap: 12px;
    height: 30px;
    font-size: 16px;
    color: var(--ink);
  }
  .contacts__icon {
    width: 22px;
    height: 22px;
    background: var(--green);
    display: flex;
    align-items: center;
    justify-content: center;
    flex: none;
  }
  .address {
    position: absolute;
    right: 46px;
    top: 238px;
    text-align: right;
    font-size: 15px;
    line-height: 20px;
    color: var(--ink);
  }
</style>
</head>
<body>
<div class="stage">

  <section class="card card--front">
    <div class="brand">
      <div class="brand__mark"></div>
      <div class="brand__name">ClearPathVitality</div>
    </div>
    <div class="front__tagline">Roots of Balance, Light of Renewal</div>
    <div class="front__web">www.clearpathvitality.com</div>
  </section>

  <section class="card card--back">
    <div class="brand">
      <div class="brand__mark"></div>
      <div class="brand__name">ClearPathVitality</div>
    </div>

    <div class="person">
      <div class="person__name"><span class="person__first">NORA</span> <span class="person__last">KETTERING</span>, <span class="person__first">PhD</span></div>
      <div class="person__title">ADVANCED INSTRUCTOR &amp; PRACTITIONER</div>
    </div>

    <div class="divider"></div>

    <ul class="contacts">
      <li>
        <span class="contacts__icon">
          <svg width="14" height="14" viewBox="0 0 24 24"><path fill="#fff" d="M6.6 10.8a15.1 15.1 0 0 0 6.6 6.6l2.2-2.2c.3-.3.7-.4 1-.2 1.1.4 2.3.6 3.6.6.6 0 1 .4 1 1V20c0 .6-.4 1-1 1A17 17 0 0 1 3 4c0-.6.4-1 1-1h3.5c.6 0 1 .4 1 1 0 1.3.2 2.5.6 3.6.1.3 0 .7-.2 1z"/></svg>
        </span>
        831-555-2746
      </li>
      <li>
        <span class="contacts__icon">
          <svg width="14" height="14" viewBox="0 0 24 24"><rect x="3" y="6" width="18" height="12" fill="none" stroke="#fff" stroke-width="2"/><path d="M3 6l9 7 9-7" fill="none" stroke="#fff" stroke-width="2"/></svg>
        </span>
        nora@clearpathvitality.com
      </li>
      <li>
        <span class="contacts__icon">
          <svg width="14" height="14" viewBox="0 0 24 24"><circle cx="12" cy="12" r="8.5" fill="none" stroke="#fff" stroke-width="2"/><path d="M3.5 12h17M12 3.5c3 3 3 14 0 17M12 3.5c-3 3-3 14 0 17" fill="none" stroke="#fff" stroke-width="1.5"/></svg>
        </span>
        www.clearpathvitality.com
      </li>
    </ul>

    <div class="address">
      418 Alder Ln, Bldg 12, Ste 305<br>
      Santa Cruz, CA 95060
    </div>
  </section>

</div>
</body>
</html>
```